New one page Homepage with registration and log in form

Hi designers!

We need a new homepage and made a skitch of how it should be.

Can you give some of your design ideas and work it out so that it actually looks great?

Its just one page, for convertion reasons.

The logo doesnt have to be changed.

It would be cool to center the logo but not sure how design technically correct that is.

The social icons can be left out.

If you could give a few mockups than we can choose the best one.

I added one screenshot sketch of the homepage.

And 2 screenshots of what the system looks like on the inside, just so you get an idea.

Thanks

Target Market(s)

Vacation rental owners who want to increase their bookings by connecting with other VR owners and managers, or by having their own booking team for a small fee.

Industry/Entity Type

Social

Number of Pages Required

1 page

Requirements
Must have
• Use your imagination please
Nice to have
• Use your imagination
• It will be a one page design so we need to impress :)
• Keep it compact, maybe a web 3.0 flat design, etc
Should not have
• Other pages.

```html
<!DOCTYPE html>
<html lang="en">
<head>
<meta charset="utf-8">
<title>StayNest – Social Booking Network</title>
<link href="https://fonts.googleapis.com/css2?family=Open+Sans:wght@400;600;700&family=Arimo:wght@400;700&display=swap" rel="stylesheet">
<style>
  :root {
    --page-bg: #eceded;
    --page-glow: #f7f8f8;
    --rule: #c9cbcc;
    --ink: #111111;
    --ink-soft: #333333;
    --blue: #0b46a8;
    --orange: #ff5a05;
    --green: #a9cf4a;
    --green-light: #bddc62;
    --field-border: #c9d3e0;
    --placeholder: #8a8a8a;
    --dash: #6f6f6f;
    --social-a: #2aa3e6;
    --social-b: #d92b25;
    --social-c: #2c4f92;
    --social-d: #1b76c4;
    --button-social: #2d58b0;
  }
  * { box-sizing: border-box; margin: 0; padding: 0; }
  html, body { width: 1200px; height: 1139px; overflow: hidden; }
  body {
    position: relative;
    font-family: "Arimo", Arial, sans-serif;
    color: var(--ink);
    background: radial-gradient(ellipse at 50% 45%, var(--page-glow) 0%, var(--page-bg) 70%);
  }
  .abs { position: absolute; }

  /* header */
  .header-rule { top: 72px; height: 1px; background: var(--rule); }
  .brand { left: 112px; top: 30px; width: 210px; }
  .brand-name {
    display: flex; align-items: center; gap: 10px;
    font-family: "Open Sans", sans-serif; font-weight: 700; font-size: 36px;
    color: var(--blue); line-height: 1;
  }
  .brand-mark { width: 26px; height: 26px; background: var(--orange); border-radius: 4px; }
  .brand-tagline {
    margin-top: 22px; font-family: "Open Sans", sans-serif; font-weight: 600;
    font-size: 18px; color: #2b2b2b; margin-left: -4px; white-space: nowrap;
  }
  .login-link {
    right: 128px; top: 17px; font-size: 17px; color: var(--ink-soft);
    display: flex; align-items: center; gap: 8px;
  }
  .social { top: 53px; width: 35px; height: 35px; border-radius: 6px; }

  /* video */
  .video-frame {
    left: 108px; top: 172px; width: 503px; height: 327px;
    background: #fff; border: 1px solid #dcdcdc;
    box-shadow: 0 1px 3px rgba(0,0,0,.08);
  }
  .video-still {
    left: 122px; top: 185px; width: 473px; height: 299px;
    background: linear-gradient(180deg, #d9dad7 0%, #8c8a86 45%, #4b5566 80%, #2f3440 100%);
  }
  .player-play {
    left: 130px; top: 438px; width: 65px; height: 38px;
    background: rgba(30,30,30,.85); border-radius: 4px;
    display: flex; align-items: center; justify-content: center;
  }
  .player-bar {
    left: 203px; top: 443px; width: 387px; height: 29px;
    background: rgba(30,30,30,.8); border-radius: 4px;
  }
  .player-track { left: 10px; top: 9px; width: 196px; height: 10px; border: 1px solid #777; }
  .player-volume { left: 216px; top: 9px; width: 32px; height: 10px; background: #1a9be0; }

  /* intro */
  .intro { left: 640px; top: 188px; width: 450px; font-size: 14px; line-height: 20px; letter-spacing: 0.3px; }
  .intro p + p { margin-top: 20px; }
  .intro .lead { font-weight: 700; }

  /* panels */
  .panels { left: 0; top: 0; }
  .panel-title {
    font-family: "Open Sans", sans-serif; font-weight: 600; font-size: 30px;
    color: #fff; text-align: center; letter-spacing: -0.3px;
  }
  .field {
    position: absolute; height: 34px; background: #fff;
    border: 1px solid var(--field-border); border-radius: 2px;
    font-size: 13px; color: var(--placeholder); padding: 10px 9px 0;
    box-shadow: inset 0 1px 2px rgba(0,0,0,.12);
  }
  .remember {
    left: 150px; top: 779px; font-size: 12px; color: #fff; letter-spacing: .3px;
    display: flex; align-items: center; gap: 6px;
  }
  .remember .box { width: 12px; height: 12px; background: #fff; border-radius: 2px; }
  .btn-login {
    left: 178px; top: 812px; width: 325px; height: 43px;
    background: linear-gradient(180deg, var(--green-light), var(--green));
    border-radius: 3px; color: #fff; font-family: "Open Sans", sans-serif;
    font-size: 18px; text-align: center; line-height: 43px;
  }
  .social-note { left: 150px; top: 873px; width: 362px; text-align: center; color: #fff; font-size: 14px; }
  .btn-social {
    left: 246px; top: 899px; width: 170px; height: 39px;
    background: linear-gradient(180deg, #3c6bc4, var(--button-social));
    border: 1px solid #6b8fd6; border-radius: 5px; color: #fff;
    font-family: "Open Sans", sans-serif; font-size: 13px;
    display: flex; align-items: center; padding-left: 12px; gap: 14px;
    box-shadow: 0 2px 3px rgba(0,0,0,.3);
  }
  .btn-social .dot { width: 10px; height: 14px; background: #fff; border-radius: 2px; }
  .forgot { left: 191px; top: 1031px; font-size: 13px; color: var(--ink); }
  .register-sub { left: 645px; top: 662px; width: 462px; text-align: center; font-size: 12px; color: var(--ink); }
  .legal { left: 640px; top: 1050px; width: 385px; font-size: 12px; line-height: 17px; color: var(--ink-soft); }
</style>
</head>
<body>

<header>
  <div class="abs header-rule" style="left:0;width:98px"></div>
  <div class="abs header-rule" style="left:331px;width:552px"></div>
  <div class="abs header-rule" style="left:1079px;width:121px"></div>

  <div class="abs brand">
    <div class="brand-name"><span class="brand-mark"></span>StayNest</div>
    <div class="brand-tagline">where hosts meet hosts</div>
  </div>

  <div class="abs login-link">Login
    <svg width="13" height="17" viewBox="0 0 13 17" aria-hidden="true">
      <path d="M3 7V4.5a3.5 3.5 0 0 1 7 0V7" fill="none" stroke="#222" stroke-width="2"/>
      <rect x="0.5" y="7" width="12" height="10" rx="1.5" fill="#222"/>
    </svg>
  </div>

  <div class="abs social" style="left:900px;background:var(--social-a)"></div>
  <div class="abs social" style="left:942px;background:var(--social-b)"></div>
  <div class="abs social" style="left:984px;background:var(--social-c)"></div>
  <div class="abs social" style="left:1026px;background:var(--social-d)"></div>
</header>

<section class="video">
  <div class="abs video-frame"></div>
  <div class="abs video-still" role="img" aria-label="Family of five on a sofa looking at tablets together"></div>
  <div class="abs player-play">
    <svg width="16" height="18" viewBox="0 0 16 18" aria-hidden="true"><path d="M1 1l14 8-14 8z" fill="#fff"/></svg>
  </div>
  <div class="abs player-bar">
    <div class="abs player-track"></div>
    <div class="abs player-volume"></div>
  </div>
</section>

<section class="abs intro">
  <p class="lead">StayNest is a new Social Booking Network.</p>
  <p>Vacation rental hosts and Property Managers can find easch other, connect and chat amongst themselves for sharing reservation inquires, services or anything you can imagine, in a convenient social environment.</p>
  <p>Managers can find easch other, connect and chat amongst them-selves for sharing reservation inquires, services or anything you can imagine, in a convenient social environment.</p>
  <p>Vacation rental hosts and Property Managers can find easch other, connect and chat amongst themselves for sharing reservation inquires, services or anything you can imagine.</p>
</section>

<svg class="abs panels" width="1200" height="1139" aria-hidden="true">
  <path d="M112 566 L580 582 L568 1012 L240 1003 L138 1050 L178 998 L97 996 Z"
        fill="none" stroke="var(--dash)" stroke-width="2" stroke-dasharray="9 6"/>
  <path d="M134 578 Q122 577 122 590 L110 972 Q110 985 124 986 L180 988 L150 1038 L232 992 L545 1002 Q558 1002 558 989 L571 605 Q572 592 560 592 Z"
        fill="var(--blue)"/>
  <path d="M636 583 L1103 579 L1106 1012 L1040 1013 L1050 1055 L960 1017 L636 1016 Z"
        fill="none" stroke="var(--dash)" stroke-width="2" stroke-dasharray="9 6"/>
  <path d="M658 596 Q645 596 645 609 L648 992 Q648 1005 661 1005 L962 1001 L1042 1046 L1028 999 L1083 999 Q1096 999 1096 986 L1093 603 Q1093 590 1080 590 Z"
        fill="var(--orange)"/>
</svg>

<section class="login-panel">
  <h2 class="abs panel-title" style="left:122px;top:613px;width:436px">Login to your Account</h2>
  <div class="field" style="left:150px;top:673px;width:381px">Your username or email address</div>
  <div class="field" style="left:150px;top:724px;width:381px">Your Password</div>
  <div class="abs remember"><span class="box"></span>Would you like us to remember you?</div>
  <div class="abs btn-login">Log Me In</div>
  <div class="abs social-note">Sign in with your social identity</div>
  <div class="abs btn-social"><span class="dot"></span>Share on Circlet</div>
  <div class="abs forgot">I forgot my username / password</div>
</section>

<section class="register-panel">
  <h2 class="abs panel-title" style="left:645px;top:615px;width:458px">Don’t have an account?</h2>
  <div class="abs register-sub">Register now to join the Free Booking Network !</div>
  <div class="field" style="left:665px;top:691px;width:196px;height:32px">First Name</div>
  <div class="field" style="left:872px;top:691px;width:202px;height:32px">Last Name</div>
  <div class="field" style="left:665px;top:735px;width:411px">Username</div>
  <div class="field" style="left:665px;top:781px;width:411px">Password</div>
  <div class="field" style="left:665px;top:826px;width:411px">user@email.com</div>
  <div class="field" style="left:665px;top:870px;width:411px">Set your contact number. Example: +12345678910</div>
  <div class="field" style="left:665px;top:916px;width:411px">Whats your reason for joining?</div>
  <p class="abs legal">Thank you for choosing StayNest, and for using our serices ("Serives"). The StayNest serices are provided by Varlen S.A.</p>
</section>

</body>
</html>
```